Business Card for Brightwave Reach

Please design a Modern Business card for a Online Marketing Company

Website: http://www.brightwavereach.com.au

Please do NOT include physical address in design.

Industry/Entity Type

Business

```html
<!DOCTYPE html>
<html lang="en">
<head>
<meta charset="utf-8">
<title>Brightwave Reach – Business Card</title>
<link href="https://fonts.googleapis.com/css2?family=Roboto:wght@400;700;900&family=Open+Sans:wght@400;600&display=swap" rel="stylesheet">
<style>
  :root {
    --brand-red: #c20017;
    --brand-orange: #f57c00;
    --paper: #ffffff;
    --ink: #222222;
    --backdrop: #ececec;
  }
  * { margin: 0; padding: 0; box-sizing: border-box; }
  html, body { width: 1200px; height: 483px; overflow: hidden; }
  body {
    background: var(--backdrop);
    display: flex;
    align-items: center;
    justify-content: center;
    gap: 50px;
    font-family: "Roboto", Arial, sans-serif;
  }
  .card {
    position: relative;
    width: 520px;
    height: 300px;
    overflow: hidden;
    box-shadow: 0 6px 18px rgba(0,0,0,0.22);
  }
  /* Front */
  .card-front { background: var(--brand-red); }
  .card-front .shape { position: absolute; inset: 0; }
  .brand-block {
    position: absolute;
    left: 30px;
    top: 146px;
    width: 230px;
  }
  .brand-name {
    font-weight: 700;
    font-size: 22px;
    color: var(--brand-red);
    display: flex;
    align-items: center;
    gap: 8px;
  }
  .brand-mark {
    width: 12px; height: 12px;
    background: var(--brand-orange);
    flex: none;
  }
  .brand-tagline {
    font-weight: 400;
    font-size: 12px;
    color: var(--ink);
    margin-top: 8px;
  }
  .person {
    position: absolute;
    right: 28px;
    top: 40px;
    text-align: right;
    color: var(--paper);
  }
  .person-name { font-weight: 700; font-size: 19px; }
  .person-title { font-weight: 700; font-size: 13px; margin-top: 2px; }
  .contact {
    position: absolute;
    right: 28px;
    top: 168px;
    list-style: none;
    color: var(--paper);
    font-family: "Open Sans", Arial, sans-serif;
    font-size: 12.5px;
    text-align: right;
  }
  .contact li {
    display: flex;
    align-items: center;
    justify-content: flex-end;
    gap: 7px;
    line-height: 22px;
  }
  .contact svg { width: 12px; height: 12px; flex: none; }
  /* Back */
  .card-back {
    background: var(--brand-red);
    color: var(--paper);
    text-align: center;
  }
  .back-name {
    position: absolute;
    top: 98px;
    width: 100%;
    font-weight: 700;
    font-size: 38px;
  }
  .back-tagline {
    position: absolute;
    top: 150px;
    width: 100%;
    font-weight: 400;
    font-size: 18px;
  }
  .back-web {
    position: absolute;
    top: 222px;
    width: 100%;
    font-family: "Open Sans", Arial, sans-serif;
    font-size: 20px;
    letter-spacing: 0.8px;
  }
</style>
</head>
<body>

  <section class="card card-front">
    <svg class="shape" viewBox="0 0 520 300" width="520" height="300" aria-hidden="true">
      <path d="M0 0 H300 Q350 150 215 300 H0 Z" fill="var(--paper)"/>
      <path d="M0 0 H293 Q340 150 207 300 H0 Z" fill="var(--brand-orange)"/>
      <path d="M0 0 H275 Q318 150 188 300 H0 Z" fill="var(--paper)"/>
    </svg>

    <div class="brand-block">
      <div class="brand-name"><span class="brand-mark"></span>Brightwave Reach</div>
      <div class="brand-tagline">Be seen online - Grow online</div>
    </div>

    <div class="person">
      <div class="person-name">Your Name</div>
      <div class="person-title">Title</div>
    </div>

    <ul class="contact">
      <li>
        <svg viewBox="0 0 12 12" aria-hidden="true"><circle cx="6" cy="6" r="6" fill="#fff"/><path d="M4 3 L5 3 L5.6 4.6 L4.9 5.2 Q5.6 6.6 6.8 7.1 L7.4 6.4 L9 7 L9 8 Q8.5 9 7.4 8.8 Q4.2 8 3.2 4.6 Q3.1 3.4 4 3 Z" fill="var(--brand-red)"/></svg>
        0400 512 907
      </li>
      <li>
        <svg viewBox="0 0 12 12" aria-hidden="true"><circle cx="6" cy="6" r="6" fill="#fff"/><rect x="3" y="4" width="6" height="4.2" fill="var(--brand-red)"/><path d="M3 4 L6 6.4 L9 4" stroke="#fff" stroke-width="0.7" fill="none"/></svg>
        plan@brightwavereach.com.au
      </li>
      <li>
        <svg viewBox="0 0 12 12" aria-hidden="true"><circle cx="6" cy="6" r="5.4" fill="none" stroke="#fff" stroke-width="1.1"/><ellipse cx="6" cy="6" rx="2.2" ry="5.4" fill="none" stroke="#fff" stroke-width="0.9"/><path d="M0.8 6 H11.2" stroke="#fff" stroke-width="0.9"/></svg>
        www.brightwavereach.com.au
      </li>
    </ul>
  </section>

  <section class="card card-back">
    <div class="back-name">Brightwave Reach</div>
    <div class="back-tagline">Be seen online - Grow online</div>
    <div class="back-web">www.brightwavereach.com.au</div>
  </section>

</body>
</html>
```